依頼詳細
PCとスマホデザインの両方納品をいただきますが、
まずはデザインイメージが確認しやすいPCページのみの提案をお願いします。
スマホページは当選者に納品時にお願いしたいと思います。
スマホサイズは横幅750pxのサイズで作成してください。

レスポンシブウェブデザインを意識したデザインでお願いします。

デザインに関しては、添付してあるデザインレイアウト設計シートを基にお願いします。
参考サイトのURLはデザインレイアウト設計シートに記載してあります。

画像データについては、既存サイトや参考サイト、フリー素材から流用してイメージ画像に当て込んでください。
足りない場合は、一旦他のサイトの写真をサンプルとして入れてください。(サンプルなどの表記をお願いします)
ページ数
1ページ
希望イメージ
シンプル 複雑
単色 カラフル
暗い 明るい
日常 高級
遊び心 厳粛
未来的 伝統的
女性的 男性的
希望する色
青系、水色系、明るい色味
納品ファイル
• 高解像度JPG (.jpg)
• イラストレーター形式 (.ai)
• フォトショップ形式 (.psd)
• PNG形式 (.png)
補足説明
上記のいずれか1つ。アウトラインありとなしの2つ。

クライアントのイメージ通りでした。

たくさんのご提案ありがとうございました。
次回もぜひ、よろしくお願い致します。

```html
<!DOCTYPE html>
<html lang="ja">
<head>
<meta charset="utf-8">
<title>ソラ・インダストリー株式会社</title>
<link href="https://fonts.googleapis.com/css2?family=Montserrat:wght@500;700&family=Noto+Sans+JP:wght@400;500;700&display=swap" rel="stylesheet">
<style>
:root{
  --blue:#1f8fd6;
  --sky:#27b2e6;
  --green:#2fb67c;
  --red:#e34a3d;
  --orange:#f39a1e;
  --ink:#333;
  --sub:#777;
  --line:#dcdcdc;
  --pale:#f2f2f2;
  --white:#fff;
}
*{margin:0;padding:0;box-sizing:border-box}
html,body{width:1200px;height:3080px;overflow:hidden}
body{font-family:"Noto Sans JP",sans-serif;color:var(--ink);background:var(--white);position:relative}
.en{font-family:"Montserrat",sans-serif}
a{text-decoration:none}

/* header */
.site-header{position:absolute;top:0;left:0;width:1200px;height:112px;background:var(--white)}
.brand{position:absolute;left:40px;top:36px;display:flex;align-items:center;gap:10px}
.brand-dot{width:40px;height:40px;border-radius:50%;background:var(--blue)}
.brand-name{font-size:30px;font-weight:700;color:var(--blue);letter-spacing:2px}
.search{position:absolute;left:760px;top:30px;width:350px;height:28px;border:1px solid var(--line);border-radius:2px}
.search svg{position:absolute;right:8px;top:6px}
.global-nav{position:absolute;right:90px;top:72px;display:flex;font-size:13px;white-space:nowrap}
.global-nav a{padding:6px 14px;color:var(--ink);border-left:1px solid var(--line);white-space:nowrap;line-height:1.4}
.global-nav a:first-child{border-left:none}
.global-nav a.current{color:var(--blue);border-bottom:2px solid var(--blue)}
.contact-btn{position:absolute;right:0;top:0;width:80px;height:112px;background:var(--orange);color:var(--white);font-size:11px;text-align:center;padding-top:40px;white-space:nowrap}
.contact-btn svg{display:block;margin:0 auto 8px}

/* hero */
.hero{position:absolute;top:112px;left:0;width:1200px;height:508px}
.hero-photo{position:absolute;inset:0;background:linear-gradient(100deg,#f4f6f8 0%,#e9edf0 45%,#d7dee3 70%,#eef1f3 100%)}
.hero-copy{position:absolute;left:150px;top:270px;font-size:30px;font-weight:700;line-height:1.5;color:var(--ink)}
.hero-copy em{font-style:normal;color:var(--white);background:var(--sky);padding:0 6px}
.hero-btn{position:absolute;left:150px;top:412px;width:190px;height:36px;border:1px solid var(--sky);color:var(--sky);background:var(--white);font-size:13px;display:flex;align-items:center;justify-content:center;white-space:nowrap}

/* section titles */
.sec-title{text-align:center}
.sec-title h2{font-family:"Montserrat",sans-serif;font-size:38px;font-weight:700;letter-spacing:4px;color:#444}
.sec-title p{font-size:13px;color:var(--sub);margin-top:2px}
.outline-btn{display:block;margin:0 auto;width:200px;height:38px;border:1px solid var(--sky);color:var(--sky);font-size:13px;text-align:center;line-height:36px;border-radius:2px;white-space:nowrap}

/* products */
.products{position:absolute;top:700px;left:0;width:1200px;height:580px}
.slider{position:absolute;top:130px;left:0;width:1200px;height:260px}
.arrow{position:absolute;top:80px}
.arrow.prev{left:125px}.arrow.next{right:125px}
.cards{position:absolute;left:160px;top:0;display:flex;gap:40px}
.card{width:200px;position:relative}
.card-photo{width:200px;height:180px}
.card-tag{display:inline-block;font-size:11px;color:var(--white);padding:2px 10px;margin-top:-10px;position:relative;left:100px;white-space:nowrap}
.card-name{font-size:13px;line-height:1.5;text-align:center;margin-top:8px}
.badge-new{position:absolute;left:10px;top:-16px;background:var(--red);color:var(--white);font-size:11px;padding:2px 8px;font-family:"Montserrat",sans-serif;font-weight:700}
.dots{position:absolute;top:466px;left:0;width:1200px;display:flex;justify-content:center;gap:10px}
.dots span{width:10px;height:10px;border-radius:50%;background:#ccc}
.dots span.on{background:var(--sky)}
.products .outline-btn{position:absolute;top:510px;left:500px}

/* information */
.information{position:absolute;top:1300px;left:0;width:1200px;height:480px}
.news{position:absolute;top:140px;left:160px;width:880px;list-style:none}
.news li{display:flex;align-items:center;height:46px;border-bottom:1px solid var(--line);font-size:13px;white-space:nowrap}
.news time{width:110px;color:var(--sub);font-family:"Montserrat",sans-serif;font-size:12px}
.news .tag{width:80px;text-align:center;color:var(--white);font-size:11px;padding:3px 0;margin-right:20px}
.tag.info{background:var(--sky)}.tag.item{background:var(--red)}
.information .outline-btn{position:absolute;top:410px;left:500px}

/* panels */
.panels{position:absolute;top:1880px;left:0;width:1200px;height:340px;display:flex}
.panel{width:400px;height:340px;color:var(--white);text-align:center;padding-top:50px}
.panel.company{background:var(--sky)}
.panel.catalog{background:var(--green)}
.panel.shop{background:var(--red)}
.panel h3{font-family:"Montserrat",sans-serif;font-size:32px;font-weight:500;letter-spacing:3px}
.panel .sub{font-size:12px;margin-top:2px}
.panel svg{display:block;margin:22px auto 20px}
.panel .desc{font-size:13px;line-height:1.7}
.panel .mini-btn{display:inline-block;margin-top:18px;width:150px;height:32px;line-height:30px;border:1px solid var(--white);font-size:12px;color:var(--white);white-space:nowrap}

/* contact */
.contact{position:absolute;top:2300px;left:0;width:1200px;height:240px}
.contact-lead{position:absolute;left:100px;top:70px}
.contact-lead h2{font-family:"Montserrat",sans-serif;font-size:30px;font-weight:700;letter-spacing:3px;color:#444}
.contact-lead p{font-size:13px;line-height:1.7;color:var(--sub);margin-top:8px}
.contact-box{position:absolute;top:0;height:240px;display:flex;flex-direction:column;align-items:center;justify-content:center;font-size:14px;gap:14px}
.contact-box.faq{left:388px;width:324px;background:#e6e6e6;color:var(--ink)}
.contact-box.form{left:748px;width:332px;background:var(--orange);color:var(--white)}

/* footer */
.site-footer{position:absolute;top:2600px;left:0;width:1200px;height:480px;background:var(--pale)}
.pagetop{position:absolute;left:570px;top:-30px;width:60px;height:30px;background:var(--pale)}
.pagetop svg{position:absolute;left:22px;top:10px}
.footer-links{position:absolute;left:100px;top:80px;display:flex;gap:60px;font-size:12px}
.footer-links ul{list-style:none}
.footer-links li{line-height:30px;white-space:nowrap}
.footer-company{position:absolute;left:720px;top:76px;display:flex;gap:18px}
.footer-company .brand-dot{width:50px;height:50px}
.footer-company .name{font-size:15px;font-weight:700}
.footer-company .addr{font-size:11px;line-height:1.8;color:var(--sub);margin-top:6px}
.copyright{position:absolute;left:0;bottom:0;width:1200px;height:50px;line-height:50px;text-align:center;font-size:11px;color:var(--sub);border-top:1px solid var(--line)}
</style>
</head>
<body>

<header class="site-header">
  <div class="brand"><span class="brand-dot"></span><span class="brand-name en">SORA</span></div>
  <div class="search">
    <svg width="16" height="16" viewBox="0 0 16 16"><circle cx="6.5" cy="6.5" r="5" fill="none" stroke="#999" stroke-width="1.6"/><line x1="10.5" y1="10.5" x2="15" y2="15" stroke="#999" stroke-width="1.6"/></svg>
  </div>
  <nav class="global-nav">
    <a class="current">ソラ・インダストリーとは</a>
    <a>商品一覧</a>
    <a>新着商品</a>
    <a>WEBカタログ</a>
    <a>会社案内</a>
  </nav>
  <a class="contact-btn">
    <svg width="26" height="18" viewBox="0 0 26 18"><rect x="1" y="1" width="24" height="16" fill="none" stroke="#fff" stroke-width="2"/><polyline points="1,1 13,10 25,1" fill="none" stroke="#fff" stroke-width="2"/></svg>
    お問い合わせ
  </a>
</header>

<section class="hero">
  <div class="hero-photo" role="img" aria-label="明るいキッチンで食器を手に取る人物の写真"></div>
  <p class="hero-copy">ソラ・インダストリーの商品が<br>日々の生活に<em>新提案</em></p>
  <a class="hero-btn">ソラ・インダストリーとは　›</a>
</section>

<section class="products">
  <div class="sec-title"><h2>PRODUCTS</h2><p>商品紹介</p></div>
  <div class="slider">
    <svg class="arrow prev" width="20" height="40" viewBox="0 0 20 40"><polyline points="18,2 2,20 18,38" fill="none" stroke="#999" stroke-width="2"/></svg>
    <div class="cards">
      <div class="card">
        <span class="badge-new">NEW</span>
        <div class="card-photo" role="img" aria-label="街並みを背景にしたボトル商品の写真" style="background:linear-gradient(160deg,#b9d4e6,#7fa8c4)"></div>
        <span class="card-tag" style="background:var(--sky)">アウトドア</span>
        <p class="card-name">折りたたみ式<br>ポータブルボトル</p>
      </div>
      <div class="card">
        <div class="card-photo" role="img" aria-label="ステンレス製の収納ラックの写真" style="background:linear-gradient(160deg,#e4e6e8,#bfc3c7)"></div>
        <span class="card-tag" style="background:var(--green)">収納用品</span>
        <p class="card-name">スチールラック<br>4段タイプ</p>
      </div>
      <div class="card">
        <div class="card-photo" role="img" aria-label="料理を盛り付けた保存容器の写真" style="background:linear-gradient(160deg,#e8c79a,#b5843f)"></div>
        <span class="card-tag" style="background:var(--orange)">キッチン用品</span>
        <p class="card-name">シリコン保存容器<br>ランチ用 3個組</p>
      </div>
      <div class="card">
        <div class="card-photo" role="img" aria-label="包丁の商品写真" style="background:linear-gradient(160deg,#f3f3f3,#d4d4d4)"></div>
        <span class="card-tag" style="background:var(--red)">キッチン用品</span>
        <p class="card-name">軽量万能包丁<br>刃渡り18cmタイプ</p>
      </div>
    </div>
    <svg class="arrow next" width="20" height="40" viewBox="0 0 20 40"><polyline points="2,2 18,20 2,38" fill="none" stroke="#999" stroke-width="2"/></svg>
  </div>
  <div class="dots"><span class="on"></span><span></span><span></span></div>
  <a class="outline-btn">商品一覧はこちら　›</a>
</section>

<section class="information">
  <div class="sec-title"><h2>INFORMATION</h2><p>お知らせ</p></div>
  <ul class="news">
    <li><time>2024.09.20</time><span class="tag info">お知らせ</span>秋季休業期間のご案内を掲載しました。ご確認ください。</li>
    <li><time>2024.09.12</time><span class="tag item">新着商品</span>キッチン用品シリーズに新しい保存容器を追加しました。</li>
    <li><time>2024.08.30</time><span class="tag info">お知らせ</span>WEBカタログ最新版の公開を開始いたしました。</li>
    <li><time>2024.08.18</time><span class="tag item">新着商品</span>アウトドア向けの新しいボトル商品を発売しました。</li>
  </ul>
  <a class="outline-btn">お知らせ一覧はこちら　›</a>
</section>

<section class="panels">
  <div class="panel company">
    <h3>COMPANY</h3><p class="sub">会社案内</p>
    <svg width="50" height="54" viewBox="0 0 50 54"><rect x="4" y="10" width="26" height="42" fill="none" stroke="#fff" stroke-width="3"/><rect x="30" y="24" width="16" height="28" fill="none" stroke="#fff" stroke-width="3"/><g fill="#fff"><rect x="10" y="17" width="5" height="5"/><rect x="19" y="17" width="5" height="5"/><rect x="10" y="28" width="5" height="5"/><rect x="19" y="28" width="5" height="5"/><rect x="10" y="39" width="5" height="5"/><rect x="19" y="39" width="5" height="5"/></g></svg>
    <p class="desc">私たちの想いと歩み、<br>事業内容をご紹介します。</p>
    <a class="mini-btn">詳細はこちら　›</a>
  </div>
  <div class="panel catalog">
    <h3>CATALOG</h3><p class="sub">WEBカタログ</p>
    <svg width="60" height="50" viewBox="0 0 60 50"><path d="M30 10 C22 4 10 4 3 7 V46 C10 43 22 43 30 48 C38 43 50 43 57 46 V7 C50 4 38 4 30 10 Z" fill="none" stroke="#fff" stroke-width="3"/><line x1="30" y1="10" x2="30" y2="48" stroke="#fff" stroke-width="3"/></svg>
    <p class="desc">全商品を掲載したカタログを<br>オンラインでご覧いただけます。</p>
    <a class="mini-btn">詳細はこちら　›</a>
  </div>
  <div class="panel shop">
    <h3>MARCHE</h3><p class="sub">マルシェショップ</p>
    <svg width="56" height="50" viewBox="0 0 56 50"><polyline points="2,4 11,4 18,34 46,34 53,12 14,12" fill="none" stroke="#fff" stroke-width="3"/><circle cx="21" cy="43" r="4" fill="#fff"/><circle cx="43" cy="43" r="4" fill="#fff"/></svg>
    <p class="desc">オンラインショップにて<br>各商品をお買い求めいただけます。</p>
    <a class="mini-btn">ご購入はこちら　›</a>
  </div>
</section>

<section class="contact">
  <div class="contact-lead">
    <h2>CONTACT</h2>
    <p>商品に関するご質問は<br>お気軽にお問い合わせください。</p>
  </div>
  <a class="contact-box faq">
    <svg width="46" height="40" viewBox="0 0 46 40"><path d="M3 3 H43 V28 H18 L8 37 V28 H3 Z" fill="none" stroke="#555" stroke-width="3"/></svg>
    よくあるご質問
  </a>
  <a class="contact-box form">
    <svg width="44" height="30" viewBox="0 0 44 30"><rect x="2" y="2" width="40" height="26" fill="none" stroke="#fff" stroke-width="3"/><polyline points="2,2 22,17 42,2" fill="none" stroke="#fff" stroke-width="3"/></svg>
    お問い合わせフォーム
  </a>
</section>

<footer class="site-footer">
  <div class="pagetop"><svg width="16" height="10" viewBox="0 0 16 10"><polyline points="1,9 8,2 15,9" fill="none" stroke="#999" stroke-width="2"/></svg></div>
  <div class="footer-links">
    <ul><li>HOME</li><li>ソラ・インダストリーとは</li><li>商品一覧</li><li>新着商品</li><li>WEBカタログ</li><li>会社案内</li></ul>
    <ul><li>お問い合わせ</li><li>よくあるご質問</li><li>リンク</li><li>個人情報保護方針</li><li>サイトマップ</li></ul>
  </div>
  <div class="footer-company">
    <span class="brand-dot"></span>
    <div>
      <p class="name">ソラ・インダストリー株式会社</p>
      <p class="addr">〒000-0000<br>架空県青空市港町1丁目2番3号<br>TEL：000-111-2222<br>FAX：000-111-3333</p>
    </div>
  </div>
  <p class="copyright">© Copyright SORA INDUSTRY Co.,Ltd. All Rights Reserved.</p>
</footer>

</body>
</html>
```